Stationary For Engineering & Consultancy Company
Harbourline Sound Consulting Inc.
Stationary For Engineering & Consultancy Company - Consulting
Professional
Rajveer Talwani
President (MSc. Applied tremolo)
42 Willowmere Crt, Brampton, Ontario L6R 3J8
info@harbourlinesound.example
www.harbourlinesound.example

```html
<!DOCTYPE html>
<html lang="en">
<head>
<meta charset="utf-8">
<title>Harbourline Sound Consulting Inc. – Business Cards</title>
<link href="https://fonts.googleapis.com/css2?family=Cinzel:wght@600&family=Open+Sans:wght@400;600&display=swap" rel="stylesheet">
<style>
  :root {
    --backdrop: #2b2c2e;
    --card: #ffffff;
    --ink: #3a3d40;
    --ink-soft: #6b6f73;
    --green: #5f9a1c;
    --green-dark: #3f7010;
    --silver: #c9cccf;
    --white: #ffffff;
  }
  * { margin: 0; padding: 0; box-sizing: border-box; }
  html, body { width: 1200px; height: 754px; overflow: hidden; }
  body {
    background: var(--backdrop);
    position: relative;
    font-family: "Open Sans", Arial, sans-serif;
    color: var(--ink);
  }
  .card {
    position: absolute;
    width: 480px;
    height: 280px;
    background: var(--card);
    box-shadow: 0 10px 26px rgba(0,0,0,.45);
    overflow: hidden;
  }
  .card-front { left: 150px; top: 80px; }
  .card-back { left: 570px; top: 390px; }

  .brand {
    display: flex;
    align-items: center;
    gap: 12px;
  }
  .brand-mark {
    width: 34px; height: 34px;
    background: var(--green);
    flex: none;
  }
  .brand-name {
    font-family: "Cinzel", Georgia, serif;
    font-weight: 600;
    color: var(--ink);
    line-height: 1.15;
  }
  .card-front .brand {
    position: absolute; left: 0; right: 0; top: 108px;
    justify-content: center;
  }
  .card-front .brand-name { font-size: 19px; width: 230px; }

  .card-back .brand {
    position: absolute; left: 26px; top: 86px;
  }
  .card-back .brand-mark { width: 26px; height: 26px; }
  .card-back .brand-name { font-size: 14px; width: 150px; }

  .contact {
    position: absolute; left: 238px; top: 42px;
  }
  .person-name {
    font-size: 12px; font-weight: 600; letter-spacing: .06em;
    text-transform: uppercase; color: var(--ink);
  }
  .person-title { font-size: 8px; color: var(--ink-soft); margin-top: 2px; }
  .contact-list { list-style: none; margin-top: 14px; }
  .contact-list li {
    display: flex; align-items: center; gap: 7px;
    font-size: 8px; color: var(--ink-soft); height: 14px;
  }
  .contact-list svg { width: 9px; height: 9px; flex: none; }

  .swoosh { position: absolute; left: 0; bottom: 0; width: 480px; height: 150px; }
  .band-address {
    position: absolute; right: 18px; bottom: 12px;
    font-size: 8px; font-weight: 600; color: var(--white); letter-spacing: .02em;
  }
</style>
</head>
<body>

  <section class="card card-front" aria-label="Business card front">
    <div class="brand">
      <span class="brand-mark"></span>
      <span class="brand-name">Harbourline Sound Consulting Inc.</span>
    </div>
  </section>

  <section class="card card-back" aria-label="Business card back">
    <svg class="swoosh" viewBox="0 0 480 150" aria-hidden="true">
      <path d="M0,104 C170,96 350,72 480,8 L480,150 L0,150 Z" fill="var(--silver)"/>
      <path d="M0,116 C170,108 350,86 480,22 L480,150 L0,150 Z" fill="var(--white)"/>
      <path d="M0,124 C170,118 350,96 480,34 L480,150 L0,150 Z" fill="var(--green)"/>
      <path d="M0,150 L0,140 C170,134 350,112 480,60 L480,64 C350,118 170,140 0,146 Z" fill="var(--green-dark)" opacity=".5"/>
    </svg>

    <div class="brand">
      <span class="brand-mark"></span>
      <span class="brand-name">Harbourline Sound Consulting Inc.</span>
    </div>

    <div class="contact">
      <p class="person-name">Rajveer Talwani</p>
      <p class="person-title">Managing Director</p>
      <ul class="contact-list">
        <li><svg viewBox="0 0 10 10"><path d="M2,1 L4,1 L4.6,3.2 L3.4,4 C4,5.3 4.7,6 6,6.6 L6.8,5.4 L9,6 L9,8 C5,8.5 1.5,5 2,1 Z" fill="var(--ink)"/></svg>416 555 0142</li>
        <li><svg viewBox="0 0 10 10"><rect x="3" y="0.5" width="4" height="9" rx="0.8" fill="var(--ink)"/></svg>416 555 0187</li>
        <li><svg viewBox="0 0 10 10"><rect x="1" y="4" width="8" height="4.5" fill="var(--ink)"/><rect x="3" y="1" width="4" height="3" fill="var(--ink)"/></svg>416 555 0199</li>
        <li><svg viewBox="0 0 10 10"><rect x="0.5" y="2" width="9" height="6" fill="var(--ink)"/><path d="M0.5,2 L5,5.5 L9.5,2" stroke="var(--white)" stroke-width="0.8" fill="none"/></svg>info@harbourlinesound.example</li>
        <li><svg viewBox="0 0 10 10"><circle cx="5" cy="5" r="4.5" fill="var(--ink)"/><path d="M0.5,5 H9.5 M5,0.5 C2.5,3 2.5,7 5,9.5 M5,0.5 C7.5,3 7.5,7 5,9.5" stroke="var(--white)" stroke-width="0.6" fill="none"/></svg>www.harbourlinesound.example</li>
      </ul>
    </div>

    <p class="band-address">42 Willowmere Crt, Brampton, Ontario L6R 3J8</p>
  </section>

</body>
</html>
```